LLC needs a business card design that emphasizes consulting and expert witness in upstream oil and g

I need a business card design for my company called Velmo Consultative Service, LLC. My expertise is in oil and gas upstream operations management to optimize performance and also as an expert witness for law firms in oil and gas upstream operations litigation.
The final design should communicate knowledge and hands-on experience as well as trust. (Velmo means rope or lasso. Perhaps "Velmo" should be in the form of a rope.) I do not like the color green in any shade. My first preference would be some shade of blue.

```html
<!DOCTYPE html>
<html lang="en">
<head>
<meta charset="utf-8">
<title>Velmo Consultative Service LLC – Business Card</title>
<link rel="stylesheet" href="https://fonts.googleapis.com/css2?family=Montserrat:wght@400;500;600;700&display=swap">
<style>
  :root {
    --stage: #e4e5e9;
    --paper: #ffffff;
    --paper-shade: #f1f1f3;
    --royal: #3a4fa6;
    --royal-deep: #2f4296;
    --sky: #4fb6e3;
    --sky-soft: #8fd0ee;
    --rule: rgba(255,255,255,0.22);
    --ink-white: #ffffff;
  }
  * { box-sizing: border-box; margin: 0; padding: 0; }
  html, body {
    width: 1200px; height: 1000px; overflow: hidden;
    background: var(--stage);
    font-family: "Montserrat", Arial, sans-serif;
  }
  .card {
    position: absolute;
    left: 220px;
    width: 760px; height: 430px;
    background: linear-gradient(135deg, var(--paper) 40%, var(--paper-shade));
    overflow: hidden;
    box-shadow: 0 10px 30px rgba(0,0,0,0.18);
  }
  .card--front { top: 45px; }
  .card--back { top: 525px; }
  .card__shape { position: absolute; inset: 0; }

  .brand {
    position: absolute;
    display: flex; flex-direction: column; align-items: center;
  }
  .card--front .brand { left: 0; right: 0; top: 120px; }
  .card--back .brand { left: 40px; width: 320px; top: 150px; }
  .brand__ring {
    width: 96px; height: 96px;
    border: 4px solid var(--royal);
    border-radius: 50%;
    margin-bottom: 22px;
  }
  .brand__name {
    font-size: 19px; font-weight: 600;
    color: var(--royal);
    letter-spacing: 0.3px;
    white-space: nowrap;
  }

  .holder {
    position: absolute; right: 40px; top: 34px; text-align: right;
  }
  .holder__name { color: var(--ink-white); font-size: 22px; font-weight: 700; }
  .holder__role { color: var(--sky-soft); font-size: 16px; font-weight: 400; margin-top: 4px; }

  .contact {
    position: absolute;
    display: flex; align-items: center;
    height: 40px;
  }
  .contact__icon {
    width: 46px; height: 30px;
    background: var(--sky);
    display: flex; align-items: center; justify-content: center;
    flex: none;
  }
  .contact__icon svg { width: 16px; height: 16px; fill: var(--ink-white); }
  .contact__text {
    margin-left: 22px;
    color: var(--ink-white);
    font-size: 17px; font-weight: 400; line-height: 1.2;
    white-space: nowrap;
  }
  .contact--address { left: 420px; top: 186px; height: 56px; }
  .contact--phone { left: 446px; top: 246px; }
  .contact--fax { left: 472px; top: 296px; }
  .contact--mail { left: 498px; top: 346px; }
</style>
</head>
<body>

<section class="card card--front" aria-label="Card front">
  <svg class="card__shape" viewBox="0 0 760 430" aria-hidden="true">
    <polygon points="380,0 760,0 760,64" fill="var(--royal)"/>
  </svg>
  <div class="brand">
    <div class="brand__ring"></div>
    <div class="brand__name">Velmo Consultative Service LLC</div>
  </div>
</section>

<section class="card card--back" aria-label="Card back">
  <svg class="card__shape" viewBox="0 0 760 430" aria-hidden="true">
    <polygon points="330,0 760,0 760,430 530,430" fill="var(--royal)"/>
    <g stroke="var(--rule)" stroke-width="1">
      <line x1="440" y1="112" x2="720" y2="112"/>
      <line x1="470" y1="244" x2="740" y2="244"/>
      <line x1="495" y1="293" x2="740" y2="293"/>
      <line x1="520" y1="343" x2="740" y2="343"/>
    </g>
  </svg>

  <div class="brand">
    <div class="brand__ring"></div>
    <div class="brand__name">Velmo Consultative Service LLC</div>
  </div>

  <div class="holder">
    <div class="holder__name">Your Name</div>
    <div class="holder__role">Owner / CEO</div>
  </div>

  <div class="contact contact--address">
    <span class="contact__icon"><svg viewBox="0 0 16 16"><path d="M8 1a5 5 0 0 0-5 5c0 3.6 5 9 5 9s5-5.4 5-9a5 5 0 0 0-5-5zm0 7a2 2 0 1 1 0-4 2 2 0 0 1 0 4z"/></svg></span>
    <span class="contact__text">Address Line 1<br>Address Line 2</span>
  </div>
  <div class="contact contact--phone">
    <span class="contact__icon"><svg viewBox="0 0 16 16"><path d="M3.6 1.5l2.3 2.6-1.2 1.8a9 9 0 0 0 5.4 5.4l1.8-1.2 2.6 2.3-1.3 2.1C7.6 14.5 1.5 8.4 1.5 2.8z"/></svg></span>
    <span class="contact__text">123 456 789</span>
  </div>
  <div class="contact contact--fax">
    <span class="contact__icon"><svg viewBox="0 0 16 16"><path d="M4 1h8v4H4zM2 6h12v6h-2v3H4v-3H2zm3 4v4h6v-4z"/></svg></span>
    <span class="contact__text">123 456 7890</span>
  </div>
  <div class="contact contact--mail">
    <span class="contact__icon"><svg viewBox="0 0 16 16"><path d="M1 3h14v10H1zm1.5 1.2V5l5.5 4 5.5-4v-.8L8 8.2z"/></svg></span>
    <span class="contact__text">admin@velmo.com</span>
  </div>
</section>

</body>
</html>
```